IT Consulting company Needs a Logo Design and Business Cards

I need a New Logo and Business Cards for an established IT Managed Services Company that specializes in flat-rate managed IT services. We provide Design and Build, Help Desk, Onsite and Remote Support Services.

Target Market(s)

Corporate Clients

Industry/Entity Type

It Company

Logo Text

Halbrook Computer Group

Requirements
Nice to have
• Tag Line= Dependable IT at Every Turn

```html
<!DOCTYPE html>
<html lang="en">
<head>
<meta charset="utf-8">
<title>Halbrook Computer Group — Business Cards</title>
<link href="https://fonts.googleapis.com/css2?family=Montserrat:wght@400;500;600;700&display=swap" rel="stylesheet">
<style>
  :root {
    --stage: #23272d;
    --card: #1f1b1c;
    --card-shade: #262223;
    --brand-blue: #34a8e0;
    --text-light: #f2f2f2;
    --text-muted: #cfcfcf;
  }
  * { margin: 0; padding: 0; box-sizing: border-box; }
  html, body {
    width: 1200px; height: 900px; overflow: hidden;
    background: var(--stage);
    font-family: "Montserrat", sans-serif;
  }
  .stage {
    width: 1200px; height: 900px;
    display: flex; flex-direction: column;
    align-items: center; justify-content: center; gap: 56px;
  }
  .card {
    position: relative;
    width: 600px; height: 343px;
    background: var(--card);
    border-radius: 26px;
    overflow: hidden;
    box-shadow: 0 18px 40px rgba(0,0,0,.45);
  }
  .card-halo {
    position: absolute;
    width: 330px; height: 330px; border-radius: 50%;
    background: var(--card-shade);
  }
  .card-front .card-halo { right: -90px; bottom: -215px; }
  .card-back .card-halo { right: -40px; bottom: -150px; }
  .front-brand, .back-brand, .contact { z-index: 1; }
  /* Front */
  .front-brand {
    position: absolute; left: 110px; top: 108px;
    display: flex; align-items: center; gap: 22px;
  }
  .brand-dot {
    width: 120px; height: 120px; border-radius: 50%;
    background: var(--brand-blue); flex: none;
  }
  .brand-stack { display: flex; flex-direction: column; gap: 12px; }
  .brand-name {
    color: var(--brand-blue); font-weight: 700;
    text-transform: uppercase; letter-spacing: 2px;
    font-size: 26px; line-height: 1.15;
  }
  .brand-tagline {
    color: var(--brand-blue); font-weight: 500;
    text-transform: uppercase; letter-spacing: 2.5px; font-size: 10px;
  }
  /* Back */
  .back-brand {
    position: absolute; left: 48px; top: 46px;
    display: flex; align-items: center; gap: 14px;
  }
  .back-brand .brand-dot { width: 62px; height: 62px; }
  .back-brand .brand-name { font-size: 16px; letter-spacing: 1.5px; }
  .contact {
    position: absolute; left: 340px; top: 150px;
    color: var(--text-light);
  }
  .contact-name { font-weight: 700; font-size: 22px; letter-spacing: .5px; }
  .contact-role { color: var(--brand-blue); font-size: 13px; margin: 2px 0 14px; }
  .contact-list { list-style: none; display: flex; flex-direction: column; gap: 9px; }
  .contact-item {
    display: flex; align-items: center; gap: 10px;
    font-size: 14px; letter-spacing: 1.5px; color: var(--text-muted);
  }
  .contact-icon { width: 12px; height: 12px; flex: none; }
</style>
</head>
<body>
<main class="stage">

  <section class="card card-front">
    <div class="card-halo"></div>
    <div class="front-brand">
      <span class="brand-dot"></span>
      <div class="brand-stack">
        <p class="brand-name">Halbrook<br>Computer Group</p>
        <p class="brand-tagline">Dependable IT at Every Turn</p>
      </div>
    </div>
  </section>

  <section class="card card-back">
    <div class="card-halo"></div>
    <div class="back-brand">
      <span class="brand-dot"></span>
      <p class="brand-name">Halbrook<br>Computer Group</p>
    </div>
    <div class="contact">
      <p class="contact-name">John Doe</p>
      <p class="contact-role">Founder</p>
      <ul class="contact-list">
        <li class="contact-item">
          <svg class="contact-icon" viewBox="0 0 12 12"><rect x="3" y="0.5" width="6" height="11" rx="1.2" fill="none" stroke="#34a8e0" stroke-width="1.3"/><circle cx="6" cy="9.4" r=".7" fill="#34a8e0"/></svg>
          088 888 8888
        </li>
        <li class="contact-item">
          <svg class="contact-icon" viewBox="0 0 12 12"><rect x="0.5" y="2" width="11" height="8" rx="1" fill="#34a8e0"/><path d="M1 2.6 6 6.6 11 2.6" fill="none" stroke="#1f1b1c" stroke-width="1"/></svg>
          email@website.com
        </li>
        <li class="contact-item">
          <svg class="contact-icon" viewBox="0 0 12 12"><circle cx="6" cy="6" r="5.5" fill="#34a8e0"/><path d="M.5 6h11M6 .5c-2.2 2.8-2.2 8.2 0 11M6 .5c2.2 2.8 2.2 8.2 0 11" fill="none" stroke="#1f1b1c" stroke-width=".8"/></svg>
          www.website.com
        </li>
      </ul>
    </div>
  </section>

</main>
</body>
</html>
```